Publisher needs a book cover design for ‘Lanterns Over the Marsh Gate’ book

We need a book cover (front, back, spine) for the 2nd edition of a book entitled ‘Lanterns Over the Marsh Gate’ and subtitled ‘the quiet geography of tidal winds, ferry routes and harbour lanterns’ (inverted commas not to be part of the title and subtitle). The author is Rupert Calloway. The publisher is Vellmark Press. The finished size of the paperback version will be the industry standard 9" x 6". There will be paperback, hardback, and e-book versions. The final number of pages is expected to be in the region 150-180 pages. Text for the back cover is not yet available, but at the bottom of the back cover should be publisher logo (rectangular) on the left and space for the ISBN bar code on the right. The circular logo should be on the spine. The design should be original and not include any stock images that have been created by someone else or may require obtaining a copyright licence to use. Symbols in common use and not copyrighted are probably ok. There are no required images, photographs or symbols except the publisher logo at the left bottom of the back cover and lower spine. Spine lettering should be UK/US style with the top of the writing nearest the front cover. The designer is free to be creative using appropriate diagrams, symbols or abstract designs. Rectangular and circular variants of the publisher logo are attached. Designers are assured that when evaluating designs absolutely no notice whatsoever is taken of a designer's Pixo Rally ranking or status; We are completely output driven, so what matters is the design, not the ranking or status of the designer. In a similar way, designs are not evaluated as 'good' or 'bad' - the winning design will be chosen after review by a design review panel and is not decided arbitrarily by a single person. All submitted designs should be capable of effective copyright assignment.

Target Market(s)

Practitioners, parents, teachers, pupils and academics concerned with child protection, safeguarding and the elimination of emotional abuse of children in the classroom

Font styles to use
Serif
Sans Serif

Requirements
Must have
• • Title, author, edition, subtitle, publisher logo
Nice to have
• • Originality, innovation
Should not have
• • Stock images or anything else requiring additional copyright discussions and negotiations.

```html
<!DOCTYPE html>
<html lang="en">
<head>
<meta charset="utf-8">
<title>Lanterns Over the Marsh Gate — Cover Spread</title>
<link rel="stylesheet" href="https://fonts.googleapis.com/css2?family=Archivo:ital,wdth,wght@1,62..125,400&family=Jost:wght@300;400;800&display=swap">
<style>
  :root {
    --paper: #f1f1f2;
    --paper-light: #fbfbfb;
    --ink: #1d1d1d;
    --ink-soft: #2a2a2a;
    --wash-gold: rgba(222, 178, 80, 0.16);
    --wash-clear: rgba(222, 178, 80, 0);
    --label: #f8f8fa;
  }
  html, body {
    margin: 0;
    padding: 0;
    overflow: hidden;
    background: var(--paper);
  }
  .cover-spread {
    position: relative;
    width: 1200px;
    height: 874px;
    overflow: hidden;
    background: linear-gradient(90deg, var(--paper) 0%, var(--paper) 55%, var(--paper-light) 100%);
    font-family: "Jost", sans-serif;
    color: var(--ink);
  }
  .artwork-wash {
    position: absolute;
    inset: 0;
    background: linear-gradient(160deg, var(--wash-clear) 20%, var(--wash-gold) 60%, var(--wash-clear) 95%);
  }

  /* Back cover */
  .blurb {
    position: absolute;
    left: 82px;
    top: 94px;
    width: 455px;
    font-family: "Archivo", sans-serif;
    font-style: italic;
    font-stretch: 66%;
    font-size: 15px;
    line-height: 18.6px;
    color: var(--ink-soft);
  }
  .blurb p { margin: 0 0 18.6px; }
  .publisher-mark {
    position: absolute;
    left: 38px;
    top: 798px;
    display: flex;
    align-items: center;
    gap: 8px;
    font-size: 22px;
    font-weight: 400;
    color: var(--ink);
  }
  .publisher-mark .dot {
    width: 30px;
    height: 30px;
    border-radius: 50%;
    background: var(--ink);
  }
  .isbn-box {
    position: absolute;
    left: 342px;
    top: 751px;
    width: 205px;
    height: 94px;
    background: var(--label);
    font-size: 11.5px;
    box-sizing: border-box;
    padding: 12px 0 0 12px;
  }

  /* Spine */
  .spine-title, .spine-author {
    position: absolute;
    left: 598px;
    writing-mode: vertical-rl;
    transform: translateX(-50%);
    white-space: nowrap;
    color: var(--ink);
  }
  .spine-title {
    top: 45px;
    font-size: 27px;
    font-weight: 400;
    letter-spacing: 0.5px;
  }
  .spine-author {
    top: 632px;
    font-size: 23px;
    font-weight: 400;
  }
  .spine-mark {
    position: absolute;
    left: 598px;
    top: 826px;
    transform: translateX(-50%);
    display: flex;
    flex-direction: column;
    align-items: center;
    gap: 2px;
    font-size: 6px;
  }
  .spine-mark .dot {
    width: 18px;
    height: 18px;
    border-radius: 50%;
    background: var(--ink);
  }

  /* Front cover */
  .title {
    position: absolute;
    left: 644px;
    top: 66px;
    margin: 0;
    font-weight: 400;
    font-size: 84px;
    line-height: 97px;
    letter-spacing: 0.5px;
    text-transform: uppercase;
    color: var(--ink);
    text-shadow: 2px 6px 6px rgba(0, 0, 0, 0.22);
  }
  .title span { display: block; }
  .subtitle {
    position: absolute;
    left: 645px;
    top: 462px;
    width: 480px;
    margin: 0;
    font-family: "Archivo", sans-serif;
    font-style: italic;
    font-stretch: 66%;
    font-size: 27px;
    line-height: 35px;
    color: var(--ink-soft);
  }
  .edition {
    position: absolute;
    right: 80px;
    top: 554px;
    margin: 0;
    font-weight: 800;
    font-size: 29px;
    color: var(--ink);
    text-shadow: 2px 5px 5px rgba(0, 0, 0, 0.25);
  }
  .author {
    position: absolute;
    right: 88px;
    top: 696px;
    margin: 0;
    text-align: right;
    font-weight: 300;
    font-size: 60px;
    line-height: 68px;
    color: var(--ink);
    text-shadow: 2px 6px 6px rgba(0, 0, 0, 0.2);
  }
  .author span { display: block; }
</style>
</head>
<body>
  <main class="cover-spread">
    <div class="artwork-wash" role="img" aria-label="Twisted golden thorned strand sweeping across the cover from the lower back to the upper front"></div>

    <section class="back-cover">
      <div class="blurb">
        <p>Lorem ipsum dolor sit amet, consectetur adipiscing elit. Pellentesque ac tempor augue, quis pretium ipsum. Vivamus sit amet nulla bibendum urna cursus tincidunt. Morbi lacus enim, aliquam nec dignissim vel, sollicitudin non lorem. Vivamus sem odio, elementum non risus nec, pharetra lobortis enim. Duis in diam a sapien suscipit iaculis in at mi. Maecenas a risus sit amet urna mattis scelerisque ut quis quam. Duis lacinia scelerisque neque eget hendrerit. Praesent quis neque eu leo vulputate tempor vel in turpis. Maecenas varius elementum malesuada. Integer interdum in augue et dignissim.</p>
        <p>Donec id pharetra diam, dapibus ultrices eros. Quisque sodales tortor vel velit gravida, non sollicitudin ipsum varius. Praesent diam dolor, cursus at sodales vel, tincidunt ac elit. Nam vulputate pretium lacus. Orci varius natoque penatibus et magnis dis parturient montes, nascetur ridiculus mus. Nullam et risus est. Nulla aliquam dolor in orci vehicula egestas sit amet sed mi. Maecenas laoreet cursus purus ut aliquet. Cras congue laoreet arcu, sodales porttitor nulla interdum et. Lorem ipsum dolor sit amet, consectetur adipiscing elit. Phasellus efficitur urna nunc, sed cursus tellus rhoncus id. Sed ut facilisis nunc. Fusce odio tortor, feugiat a porta et, rhoncus egestas augue.</p>
      </div>
      <div class="publisher-mark"><span class="dot"></span><span>VELLMARK PRESS</span></div>
      <div class="isbn-box">ISBN</div>
    </section>

    <section class="spine">
      <div class="spine-title">LANTERNS OVER THE MARSH GATE</div>
      <div class="spine-author">Rupert Calloway</div>
      <div class="spine-mark"><span class="dot"></span><span>VELLMARK</span></div>
    </section>

    <section class="front-cover">
      <h1 class="title"><span>Lanterns</span><span>Over the</span><span>Marsh</span><span>Gate</span></h1>
      <p class="subtitle">the quiet geography of tidal winds, ferry routes and harbour lanterns</p>
      <p class="edition">2nd edition</p>
      <p class="author"><span>Rupert</span><span>Calloway</span></p>
    </section>
  </main>
</body>
</html>
```